Verlune Magician

I want the business card for my business to give to people who watch that later I will be employed to show magic here is my website http://www.verlunemagicien-exemple.fr/I want the interesting design , i am very opened for formal and informal, I watch a lot of design so don't stick to the common shape and form but i hope it can also be produced the thing to write on will be the same as in picture that i will upload , i also will upload the logo for you that so can be easy to useDenis CostilleMagicianMAGICIAN VERLUNE 17 rue des Tilleuls - 71460 SAINT-ORVAL contact@verlunemagicien-exemple.fr tel. 0381 476 093 tel. 0664 219 570

```html
<!DOCTYPE html>
<html lang="fr">
<head>
<meta charset="utf-8">
<title>Verlune Magicien – Carte de visite</title>
<link href="https://fonts.googleapis.com/css2?family=Questrial&display=swap" rel="stylesheet">
<style>
  :root {
    --page: #eeeeee;
    --card: #ffffff;
    --ink: #1a1a1a;
    --ink-soft: #333333;
    --figure-dark: #151515;
    --figure-mid: #3a3a3a;
    --card-shadow: rgba(0, 0, 0, 0.12);
  }
  html, body {
    margin: 0;
    padding: 0;
    width: 1200px;
    height: 800px;
    overflow: hidden;
    background: var(--page);
    font-family: "Questrial", "Century Gothic", sans-serif;
    color: var(--ink);
  }
  .stage {
    width: 1200px;
    height: 800px;
    display: flex;
    align-items: center;
    justify-content: center;
    gap: 60px;
  }
  .card {
    position: relative;
    width: 530px;
    height: 342px;
    background: var(--card);
    box-shadow: 0 6px 18px var(--card-shadow);
    box-sizing: border-box;
  }
  .contact {
    position: absolute;
    left: 40px;
    top: 38px;
  }
  .contact__name {
    font-size: 27px;
    letter-spacing: 1px;
    margin: 0;
    font-weight: 400;
  }
  .contact__role {
    font-size: 11px;
    letter-spacing: 0.5px;
    margin: 4px 0 22px;
  }
  .contact__block {
    font-size: 13px;
    line-height: 1.55;
    margin: 0 0 18px;
    color: var(--ink-soft);
  }
  .contact__block--links {
    font-size: 14px;
  }
  .figure {
    position: absolute;
    background: linear-gradient(160deg, var(--figure-mid), var(--figure-dark));
    border-radius: 40px 40px 6px 6px;
  }
  .card--front .figure {
    right: 40px;
    top: 130px;
    width: 160px;
    height: 122px;
  }
  .brand {
    position: absolute;
    text-align: center;
    line-height: 1;
  }
  .brand__name {
    display: block;
    font-size: 30px;
    letter-spacing: 2px;
    color: var(--ink);
  }
  .brand__role {
    display: block;
    font-size: 8px;
    letter-spacing: 1.5px;
    margin-top: 4px;
    color: var(--ink);
  }
  .card--front .brand {
    right: 30px;
    top: 260px;
    width: 180px;
  }
  .card--back .figure {
    left: 50%;
    top: 86px;
    width: 140px;
    height: 110px;
    transform: translateX(-50%);
  }
  .card--back .brand {
    left: 50%;
    top: 204px;
    width: 170px;
    transform: translateX(-50%);
  }
  .card--back .brand__name {
    font-size: 24px;
  }
</style>
</head>
<body>
  <main class="stage">
    <section class="card card--front">
      <div class="contact">
        <h1 class="contact__name">LUCIEN MARBEC</h1>
        <p class="contact__role">MAGICIEN</p>
        <p class="contact__block">17 rue des Tilleuls<br>71460 SAINT-ORVAL</p>
        <p class="contact__block contact__block--links">0522 476 093<br>0775 219 570<br>contact@verlunemagicien-exemple.fr<br>www.verlunemagicien-exemple.fr</p>
      </div>
      <div class="figure" role="img" aria-label="Black and white illustration of the magician in a dark jacket holding a playing card"></div>
      <div class="brand">
        <span class="brand__name">VERLUNE</span>
        <span class="brand__role">MAGICIEN</span>
      </div>
    </section>

    <section class="card card--back">
      <div class="figure" role="img" aria-label="Black and white illustration of the magician in a dark jacket holding a playing card"></div>
      <div class="brand">
        <span class="brand__name">VERLUNE</span>
        <span class="brand__role">MAGICIEN</span>
      </div>
    </section>
  </main>
</body>
</html>
```